Marketing company needs business card design

Our company (Bright Harbor Partners) need a business card design for a marketing company. The design should of course include the logo and business colors (orange and blue). I would like the design to be clean and professional. The business card is going to be a die cut card that is leaf shaped (I have uploaded the template for it). I would love to see a design that is professional but nothing too "corporate."
Updates

Hello everyone,

Just wanted to let you know that I have uploaded an AI and EPS version of the logo for your convenience.

Thank you!

~Miranda

Industry/Entity Type

Marketing

Requirements
Must have
• Must have the following contact info:

Bright Harbor Partners
2871 Cedar Hollow Rd B204
Prescott, AZ 86301

928.614.3827

info@brightharborpartners-example.com

```html
<!DOCTYPE html>
<html lang="en">
<head>
<meta charset="utf-8">
<title>Bright Harbor Partners – Business Card</title>
<link href="https://fonts.googleapis.com/css2?family=Ubuntu:wght@400;500&display=swap" rel="stylesheet">
<style>
  :root {
    --backdrop: #5d5d5d;
    --card-orange: #e9a254;
    --card-white: #fbfbfb;
    --brand-blue: #1a9ad6;
    --brand-orange: #e9a254;
    --ink: #1e1e1e;
  }
  * { margin: 0; padding: 0; box-sizing: border-box; }
  html, body {
    width: 1200px;
    height: 900px;
    overflow: hidden;
    background: var(--backdrop);
    font-family: "Ubuntu", sans-serif;
  }
  .canvas {
    position: relative;
    width: 1200px;
    height: 900px;
  }
  .card {
    position: absolute;
    left: 300px;
    width: 600px;
    height: 343px;
    box-shadow: 0 10px 28px rgba(0,0,0,0.35);
  }
  .card-front {
    top: 70px;
    background: var(--card-orange);
    border-radius: 0 130px 0 130px;
  }
  .card-back {
    top: 480px;
    background: var(--card-white);
    border-radius: 130px 0 130px 0;
    color: var(--ink);
  }
  .brand-lockup {
    position: absolute;
    left: 150px;
    top: 146px;
    display: flex;
    align-items: center;
    gap: 14px;
  }
  .brand-dot {
    width: 40px;
    height: 40px;
    border-radius: 50%;
    background: var(--card-white);
  }
  .brand-name {
    font-size: 32px;
    font-weight: 500;
    color: var(--brand-blue);
    letter-spacing: 0.2px;
  }
  .back-mark {
    position: absolute;
    right: 58px;
    top: 36px;
    width: 70px;
    height: 70px;
    border-radius: 50%;
    background: var(--brand-orange);
  }
  .holder {
    position: absolute;
    left: 48px;
    top: 72px;
    font-size: 20px;
    letter-spacing: 0.3px;
  }
  .holder .role {
    font-size: 14px;
  }
  .rule {
    position: absolute;
    left: 48px;
    right: 48px;
    height: 2px;
  }
  .rule-blue { background: var(--brand-blue); }
  .rule-orange { background: var(--brand-orange); height: 1px; }
  .contact-line {
    position: absolute;
    left: 48px;
    font-size: 14.5px;
  }
  .contact-line .gap { margin-left: 14px; }
  .website .domain { color: var(--brand-blue); }
</style>
</head>
<body>
<main class="canvas">
  <section class="card card-front" aria-label="Card front">
    <div class="brand-lockup">
      <span class="brand-dot"></span>
      <span class="brand-name">Bright Harbor Partners</span>
    </div>
  </section>

  <section class="card card-back" aria-label="Card back">
    <span class="back-mark"></span>
    <p class="holder">DANA WHITFIELD / <span class="role">Operation Manager</span></p>
    <div class="rule rule-blue" style="top:158px"></div>
    <p class="contact-line" style="top:170px">2871 Cedar Hollow Rd B204, Prescott, AZ 86301</p>
    <div class="rule rule-blue" style="top:200px"></div>
    <p class="contact-line" style="top:212px">Telephone: 928.614.3827<span class="gap">Email: info@brightharborpartners-example.com</span></p>
    <div class="rule rule-orange" style="top:241px"></div>
    <p class="contact-line website" style="top:262px">www.<span class="domain">brightharborpartners-example</span>.com</p>
    <div class="rule rule-blue" style="top:292px"></div>
  </section>
</main>
</body>
</html>
```